Need Business Cards for my Business

email address: rkpmarlowhollowworks@vendrimail.com
web address: rkpmarlowhollowworks.net
Slogan: We offer various QVN licenses
Rowland K. Pemberly
Please stick with colors of Company Logo
would like the card to be more of the color example of the logo.
If you need PDF copy of logo email me at the above account.
Creative control rests with you.

Industry/Entity Type

Business

Contact Information for Business Card

I am a minimalist, but would like something to pop and stand out amongst other cards, make it memorable.

Font styles to use
Serif
Decorative
Script

```html
<!DOCTYPE html>
<html lang="en">
<head>
<meta charset="utf-8">
<title>RKP Marlow Hollow Works – Business Card</title>
<link href="https://fonts.googleapis.com/css2?family=Playfair+Display:wght@400;700&family=Lora:wght@400&family=Great+Vibes&display=swap" rel="stylesheet">
<style>
  :root {
    --bg: #3a3a3a;
    --navy: #13375f;
    --blue: #1478bd;
    --mid-blue: #1a5d98;
    --red: #e8222b;
    --ink: #2b2b2b;
    --rule: #2a6db5;
    --white: #ffffff;
    --paper-grey: #d9dadc;
  }
  * { box-sizing: border-box; margin: 0; padding: 0; }
  html, body {
    width: 1200px; height: 1200px; overflow: hidden;
    background: var(--bg);
    font-family: "Playfair Display", Georgia, serif;
  }
  .card {
    position: absolute;
    left: 227px;
    width: 747px;
    height: 424px;
    border-radius: 18px;
    overflow: hidden;
  }
  .card--front {
    top: 144px;
    background: linear-gradient(135deg, var(--paper-grey) 0%, #f3f3f4 40%, var(--white) 62%);
  }
  .card--back {
    top: 634px;
    background: linear-gradient(180deg, var(--navy) 0%, var(--mid-blue) 50%, var(--blue) 75%, var(--blue) 100%);
  }
  .brand {
    position: absolute;
    left: 45px; top: 44px;
    color: var(--navy);
    font-weight: 700;
    text-transform: uppercase;
    line-height: 1;
  }
  .brand__initials { display: block; font-size: 64px; letter-spacing: 2px; }
  .brand__words { display: block; font-size: 20px; letter-spacing: 1.5px; margin-top: 8px; }
  .accent-panel {
    position: absolute; top: 0; right: 0; width: 150px; height: 100%;
    background: linear-gradient(180deg, var(--blue), var(--navy));
  }
  .accent-stripe {
    position: absolute; top: 0; right: 166px; width: 18px; height: 100%;
    background: var(--red);
  }
  .holder-name {
    position: absolute; left: 45px; top: 240px;
    color: var(--red); font-weight: 700; font-size: 34px; line-height: 44px;
  }
  .divider {
    position: absolute; left: 45px; top: 310px; width: 451px; height: 2px;
    background: var(--rule);
  }
  .contact { position: absolute; left: 45px; top: 322px; list-style: none; }
  .contact__item {
    display: flex; align-items: center; gap: 8px;
    color: var(--ink); font-family: "Lora", Georgia, serif;
    font-weight: 400; font-size: 20px; line-height: 30px;
  }
  .contact__icon { width: 20px; height: 20px; flex: none; }
  .brand--reverse {
    position: absolute; left: 0; right: 0; top: 130px;
    display: flex; align-items: center; justify-content: center; gap: 22px;
    color: var(--white); font-weight: 700; text-transform: uppercase;
  }
  .brand--reverse .brand__mark {
    width: 64px; height: 64px; border-radius: 50%; background: var(--white);
  }
  .brand--reverse .brand__text { line-height: 1; }
  .brand--reverse .brand__initials { font-size: 74px; letter-spacing: 2px; }
  .brand--reverse .brand__words { font-size: 21px; letter-spacing: 1.5px; margin-top: 8px; }
  .slogan {
    position: absolute; left: 0; right: 0; top: 282px;
    text-align: center; color: var(--white);
    font-family: "Great Vibes", cursive; font-size: 38px; line-height: 44px;
  }
</style>
</head>
<body>
  <section class="card card--front" aria-label="Business card front">
    <div class="accent-panel"></div>
    <div class="accent-stripe"></div>
    <div class="brand">
      <span class="brand__initials">RKP</span>
      <span class="brand__words">Marlow Hollow Works</span>
    </div>
    <h1 class="holder-name">Rowland K. Pemberly</h1>
    <div class="divider"></div>
    <ul class="contact">
      <li class="contact__item">
        <svg class="contact__icon" viewBox="0 0 20 20" aria-hidden="true">
          <rect x="1" y="4" width="18" height="12" fill="#1a5d98"/>
          <path d="M1 4 L10 11 L19 4 M1 16 L8 9.5 M19 16 L12 9.5" stroke="#fff" stroke-width="1.3" fill="none"/>
        </svg>
        rkpmarlowhollowworks@vendrimail.com
      </li>
      <li class="contact__item">
        <svg class="contact__icon" viewBox="0 0 20 20" aria-hidden="true">
          <g stroke="#1a5d98" stroke-width="1.4" fill="none">
            <circle cx="10" cy="10" r="8.5"/>
            <ellipse cx="10" cy="10" rx="4" ry="8.5"/>
            <path d="M1.5 10 H18.5 M3 5.5 H17 M3 14.5 H17 M10 1.5 V18.5"/>
          </g>
        </svg>
        rkpmarlowhollowworks.net
      </li>
    </ul>
  </section>

  <section class="card card--back" aria-label="Business card back">
    <div class="brand--reverse">
      <span class="brand__mark"></span>
      <div class="brand__text">
        <span class="brand__initials">RKP</span>
        <span class="brand__words">Marlow Hollow Works</span>
      </div>
    </div>
    <p class="slogan">We offer various QVN licenses</p>
  </section>
</body>
</html>
```